Business Cards for new orthopaedic surgery practice

My husband and I are starting our own orthopaedic surgery practice. We are looking for a business card that is uniform, but one will have my name/title and the other will have his. You can just create one design with my name on it for now. But when I choose your design as the winning design I will ask that you add another copy with his name/title.

We are looking for classy, simple, elite all in one. We like dark blues/a little gold/yellow. Something that goes with our logo. We want our logo incorporated. Here is all the info you need:
Business name: RV Spine & Vitality Center
Location: 38157 North Harbor Blvd
Coral Springs, FL 33058
Phone: 954-218-4630
Fax: 954-581-2473
Email: info@myrvspine.example

Names: Lorena Vickers, M.D.
Board Certified Hand and Upper Extremity Surgeon

Eban Sorley, M.D.
Board Certified Hip & Knee Replacement/General Orthopaedic Surgeon

Can decide what you want to put on the back. Maybe a slogan:
Steady Hands. Strong Recovery.

I am just going to upload our logo. The only thing is if we select you as the winning design, the location, and phone numbers may change. We will need your help to update that once fully solidified.

Industry/Entity Type

Medical

Contact Information for Business Card

Colors
0054AA
0677BA
7BADD7
CADEEF
E8F1F8
0094D4
00A9DD
6FCCEA
C7EBF8
E9F6FB

Requirements
Must have
• class, appeal,
Should not have
• We want to air on the side of masculine if we are looking at masculine vs. feminine feel. But we still want it classy, sophisticated, and something we will love

```html
<!DOCTYPE html>
<html lang="en">
<head>
<meta charset="utf-8">
<title>RV Spine &amp; Vitality Center – Business Cards</title>
<link rel="stylesheet" href="https://fonts.googleapis.com/css2?family=DM+Serif+Display&family=Poppins:wght@400;500&display=swap">
<style>
  :root {
    --backdrop: #1c1d20;
    --navy: #1b2852;
    --gold: #c79a45;
    --paper: #ffffff;
    --ink: #1d2233;
  }
  * { margin: 0; padding: 0; box-sizing: border-box; }
  html, body { width: 1200px; height: 900px; overflow: hidden; }
  body { background: var(--backdrop); position: relative; font-family: "Poppins", sans-serif; }

  .card {
    position: absolute;
    width: 560px;
    height: 320px;
    border-radius: 22px;
    overflow: hidden;
  }

  /* Back side */
  .card-back {
    left: 360px; top: 90px;
    background: var(--navy);
    color: var(--paper);
  }
  .back-brand {
    position: absolute;
    left: 0; right: 0; top: 88px;
    display: flex; flex-direction: column; align-items: center; gap: 14px;
  }
  .brand-dot {
    width: 22px; height: 22px; border-radius: 50%;
    border: 2px solid var(--gold);
  }
  .brand-name {
    font-family: "DM Serif Display", serif;
    font-size: 30px;
    letter-spacing: 1px;
    text-align: center;
    line-height: 1.15;
  }
  .card-back .brand-name { color: var(--paper); }
  .slogan {
    position: absolute;
    left: 0; right: 0; bottom: 44px;
    text-align: center;
    font-size: 14px;
    letter-spacing: 0.5px;
  }

  /* Front side */
  .card-front {
    left: 280px; top: 500px;
    background: var(--paper);
    color: var(--ink);
  }
  .front-brand {
    position: absolute;
    left: 30px; top: 100px; width: 220px;
    display: flex; flex-direction: column; align-items: center; gap: 12px;
  }
  .card-front .brand-name { color: var(--navy); font-size: 27px; }
  .details {
    position: absolute;
    left: 275px; top: 32px; right: 24px;
  }
  .doctor-name {
    font-family: "DM Serif Display", serif;
    font-weight: 400;
    color: var(--gold);
    font-size: 21px;
    line-height: 1.1;
  }
  .doctor-title {
    font-size: 11.5px;
    line-height: 1.3;
    margin-bottom: 10px;
  }
  .contact-list { list-style: none; margin-top: 4px; }
  .contact-list li {
    display: flex; align-items: center; gap: 8px;
    font-size: 12px; line-height: 1.55;
  }
  .contact-icon { width: 11px; height: 11px; fill: var(--gold); flex: none; }
  .address { font-size: 12px; line-height: 1.4; margin-top: 8px; }
</style>
</head>
<body>

<section class="card card-back">
  <div class="back-brand">
    <span class="brand-dot"></span>
    <div class="brand-name">RV Spine &amp;<br>Vitality Center</div>
  </div>
  <p class="slogan">Steady Hands. Strong Recovery.</p>
</section>

<section class="card card-front">
  <div class="front-brand">
    <span class="brand-dot"></span>
    <div class="brand-name">RV Spine &amp;<br>Vitality Center</div>
  </div>

  <div class="details">
    <h2 class="doctor-name">Lorena Vickers, M.D.</h2>
    <p class="doctor-title">Board Certified Hand and<br>Upper Extremity Surgeon</p>

    <h2 class="doctor-name">Eban Sorley, M.D.</h2>
    <p class="doctor-title">Board Certified Hip &amp; Knee Replacement<br>/General Orthopaedic Surgeon</p>

    <ul class="contact-list">
      <li>
        <svg class="contact-icon" viewBox="0 0 12 12"><path d="M1 4c0-2 2-3 5-3s5 1 5 3v1H8V4H4v1H1z M2 6h8l1 5H1z"/></svg>
        954-218-4630
      </li>
      <li>
        <svg class="contact-icon" viewBox="0 0 12 12"><rect x="3" y="1" width="6" height="3"/><rect x="1" y="4" width="10" height="5" rx="1"/><rect x="3" y="8" width="6" height="3"/></svg>
        954-581-2473
      </li>
      <li>
        <svg class="contact-icon" viewBox="0 0 12 12"><path d="M1 2h10v8H1z M1 2l5 4 5-4" stroke="#fff" stroke-width="0.8"/></svg>
        info@myrvspine.example
      </li>
      <li>
        <svg class="contact-icon" viewBox="0 0 12 12"><circle cx="6" cy="6" r="5"/></svg>
        www.harborlinebuild.example
      </li>
    </ul>

    <p class="address">38157 North Harbor Blvd<br>Coral Springs, FL 33058</p>
  </div>
</section>

</body>
</html>
```